Tech business card design

We need an amazing business card design for our new business 'Brakka' a marketing tech startup based in Sydney, Australia. We provide an online marketplace for businesses to search and buy advertising media, connect with service providers and learn more about marketing. We wish to communicate 'cool tech', reliability and professionalism and design based around our logo.

Target Market(s)

Business Owners

Contact Information for Business Card

Name
Position
Email Address
Website
Phone Number

Font styles to use
Other font styles liked:
• Avenir & Avenir Next

Colors

Designer to choose colors to be used in the design.

```html
<!DOCTYPE html>
<html lang="en">
<head>
<meta charset="utf-8">
<title>Brakka Business Card</title>
<link rel="stylesheet" href="https://fonts.googleapis.com/css2?family=Lato:wght@700;900&family=Open+Sans:wght@400;600&display=swap">
<style>
  :root {
    --backdrop: #e9e6e1;
    --navy: #0e0e3c;
    --paper: #ffffff;
    --ink-light: #ffffff;
    --rule: rgba(255,255,255,0.55);
    --shadow: 0 3px 6px rgba(0,0,0,0.35);
  }
  html, body {
    margin: 0;
    padding: 0;
    width: 1200px;
    height: 900px;
    overflow: hidden;
    background: var(--backdrop);
  }
  .canvas {
    position: relative;
    width: 1200px;
    height: 900px;
  }
  .card {
    position: absolute;
    box-shadow: var(--shadow);
  }
  .card-front {
    left: 330px;
    top: 90px;
    width: 555px;
    height: 343px;
    background: var(--navy);
    color: var(--ink-light);
    text-align: center;
  }
  .card-back {
    left: 330px;
    top: 469px;
    width: 559px;
    height: 343px;
    background: var(--paper);
    display: flex;
    align-items: center;
    justify-content: center;
  }
  .person-name {
    position: absolute;
    top: 100px;
    width: 100%;
    margin: 0;
    font-family: 'Lato', sans-serif;
    font-weight: 700;
    font-size: 20px;
    letter-spacing: 0.2px;
  }
  .person-role {
    position: absolute;
    top: 124px;
    width: 100%;
    margin: 0;
    font-family: 'Open Sans', sans-serif;
    font-size: 16px;
  }
  .divider {
    position: absolute;
    top: 164px;
    left: 207px;
    width: 167px;
    height: 1px;
    background: var(--rule);
  }
  .contact-list {
    position: absolute;
    top: 182px;
    width: 100%;
    margin: 0;
    padding: 0;
    list-style: none;
    font-family: 'Open Sans', sans-serif;
    font-size: 16px;
    line-height: 20px;
  }
  .contact-list .label { font-weight: 600; }
  .brand-name {
    margin: 0 0 0 -14px;
    font-family: 'Lato', sans-serif;
    font-weight: 900;
    font-size: 100px;
    letter-spacing: -1px;
    color: var(--navy);
    line-height: 1;
  }
</style>
</head>
<body>
  <main class="canvas">
    <section class="card card-front" aria-label="Business card front">
      <h1 class="person-name">MARCUS REILLY</h1>
      <p class="person-role">Managing Director</p>
      <div class="divider"></div>
      <ul class="contact-list">
        <li><span class="label">P:</span> 044-987 654 321</li>
        <li><span class="label">E:</span> hello@brakka.com</li>
        <li><span class="label">W:</span> www.brakkamedia.com</li>
      </ul>
    </section>
    <section class="card card-back" aria-label="Business card back">
      <p class="brand-name">brakka</p>
    </section>
  </main>
</body>
</html>
```